Refinery Service Website (Wholesale) – Luxurious Landing Pages & Industry Hub

We are seeking talented designers to create a luxurious and professional redesign for the wholesale section of our refinery service website, Halvorn KBT. Our current refinery page (https://halvornkbt.example/refinery/) and dental landing page (https://halvornkbt.example/refinery/dental-gold/) provide functional starting points with existing content (words, sections, trust badges, and video placeholders) that must be retained and enhanced with a sophisticated, high-end aesthetic. We serve high-net-worth wholesale clients across industries such as dental practices, mortuaries, estate attorneys, dentists, pawnshops, jewelry stores, and financial advisors. The project includes designing a revamped main wholesale landing page, individual landing pages for each industry with specific sections, and a central hub page to showcase these industries in an SEO-friendly and user-focused way, all while elevating the design to a luxurious standard.

Project Overview
Our refinery service specializes in precious metals and serves a variety of industries through wholesale access. We want the wholesale section of our website to exude sophistication and exclusivity while preserving and enhancing the existing content on our pages. Currently:
• Our refinery page (https://halvornkbt.example/refinery/) provides a basic overview of our services with text, sections, and trust badges, but it lacks visual appeal and a high-end feel.
• Our dental landing page (https://halvornkbt.example/refinery/dental-gold/) targets dental professionals with relevant messaging, sections, and content, but it also feels utilitarian and could benefit from a more elegant design, improved layout, and stronger calls-to-action.
Designers must use the existing words, sections, trust badges, and video placeholders from these pages as a foundation, enhancing them with a luxurious redesign and adding the additional sections specified below. We admire the clean and professional look of https://www.torvelworks.example/, but we aim to elevate our design with a more luxurious and exclusive feel to attract discerning wholesale clients. The redesign will involve:
1 Main Wholesale Landing Page: A complete overhaul of our current refinery page into a luxurious and professional entry point, retaining and enhancing existing content while improving the overall design.
2 Industry-Specific Landing Pages: A dedicated landing page for each of the following industries: dental practices, mortuaries, estate attorneys, dentists, pawnshops, jewelry stores, and financial advisors. Each page must retain and enhance existing content (where applicable) and include specific sections (detailed below) to build trust, provide information, and encourage engagement.
3 Industry Hub Page: A central page that showcases all the industries we serve in a visually appealing and SEO-optimized manner, acting as a gateway to each industry-specific landing page.
Our website is built on WordPress using the Bricks Builder, so design submissions should be provided in HTML, CSS, or as a Figma file for seamless integration. The design must be responsive, visually striking, and optimized for usability across all devices (desktop, tablet, mobile).
Project Scope
We are looking for design submissions that include:
• Main Wholesale Landing Page: A redesigned version of our current refinery page (https://halvornkbt.example/refinery/), transformed into a luxurious and professional entry point for our wholesale services. The new design must retain the existing words, sections, trust badges, and any video placeholders, enhancing them with a high-end aesthetic while improving layout and engagement.
• Industry-Specific Landing Pages: A dedicated landing page for each of the following industries: dental practices, mortuaries, estate attorneys, dentists, pawnshops, jewelry stores, and financial advisors. Each page must:
◦ Retain and enhance existing content (words, sections, trust badges, video placeholders) from pages like our dental landing page (https://halvornkbt.example/refinery/dental-gold/) as a reference, adapting it for each industry. For industries without existing pages, mirror the structure and content style of the dental page while tailoring the messaging and visuals.
◦ Include the following additional sections to enhance functionality and trust:
Trust Badges: A section displaying trust signals (e.g., certifications, accreditations, years in business) to build credibility with visitors. Include placeholders for 4–6 badges/icons, enhancing any existing badges from our current pages.
Testimonials: A section featuring 3–5 customer testimonials with placeholders for quotes, names, and industries (e.g., “Dr. Wesley Brandt, Dental Practice Owner”). If testimonials exist on current pages, enhance their presentation.
Contact Information: A clearly visible section with contact details (e.g., phone number, email, address) styled to match the luxurious aesthetic, improving any existing contact info presentation.
Contact Fillout Form: A user-friendly form for inquiries, including fields for name, email, industry, and message, with a professional design that encourages submissions, enhancing any existing forms.
Shipping Information: A section detailing shipping instructions and processes (e.g., how to send materials for refining), presented clearly and concisely, building on any existing shipping details.
Summary Service Bullet Points: A concise list of 5–7 key services or benefits tailored to the specific industry (e.g., “Fast turnaround for dental scrap” for dental pages, “Secure handling for jewelry inventory” for jewelers), improving any existing bullet points.
Video: Shipping Instructions: A placeholder for a video explaining how to ship materials to us, styled with a play button and a luxurious frame, enhancing any existing video placeholders.
Video: How Our Refinery Works: A placeholder for a video detailing our refining process, designed to match the aesthetic of the page, enhancing any existing video placeholders.
Video: Who We Are: A placeholder for a video introducing our company and values, presented in an elegant and professional manner, enhancing any existing video placeholders.
◦ Include tailored messaging and design elements that resonate with the specific industry (e.g., dental tools and scrap refining benefits for dental pages, elegant estate visuals for attorneys, jewelry displays for jewelers).
◦ Maintain a cohesive design that ties back to the overall luxurious aesthetic of the wholesale section.
• Industry Hub Page: A central hub page that showcases all the industries we serve in an SEO-friendly and visually engaging way. This page should include:
◦ A grid, carousel, or categorized layout featuring each industry with a concise description or tagline (e.g., “Dental Practices: Turn Scrap into Profit”).
◦ Links to each industry-specific landing page for easy navigation.
◦ Design elements that encourage exploration (e.g., hover effects, icons, or visuals representing each industry).
◦ SEO optimization through keyword-rich headings, meta-friendly layouts, and content areas that naturally incorporate industry terms.
• SEO and User Engagement Focus: The design should balance aesthetics with functionality, ensuring that both the hub page and individual landing pages are optimized for search engines (e.g., through clear headings, meta-friendly layouts) and capture user attention with compelling calls-to-action (e.g., “Discover Refinery Solutions for Your Dental Practice” or “Maximize Value for Your Jewelry Inventory”).
Design Requirements
• Aesthetic: Luxurious, elegant, and professional, with a focus on high-net-worth wholesale clients. The current designs (https://halvornkbt.example/refinery/ and https://halvornkbt.example/refinery/dental-gold/) are too basic and functional; we want a high-end look that conveys prestige and trust, using elements like deep golds, silvers, blacks, or whites to evoke luxury while enhancing existing content.
• Typography: Clean, modern, and sophisticated fonts that enhance readability and align with a high-end brand image, improving upon existing typography.
• Imagery: Incorporate placeholders for high-quality imagery relevant to each industry (e.g., dental tools, jewelry displays, legal documents). No stock images required in submissions—just placeholders. Retain and enhance any existing imagery placeholders from our current pages.
• Video Placeholders: Video sections (for shipping instructions, how the refinery works, and who we are) should include placeholders with play buttons and elegant frames that match the luxurious aesthetic, enhancing any existing video placeholders on our current pages.
• Responsiveness: The design must be fully responsive and look great on desktop, tablet, and mobile devices.
• SEO Optimization: The layout should support SEO best practices, such as clear heading structures (H1, H2, etc.), alt-text-friendly image placeholders, and keyword-rich content areas for each industry, building on existing content for SEO purposes.
• Deliverables Format: Submissions should include design files in HTML, CSS, or Figma format, ready for integration into WordPress with Bricks Builder.

Submission Guidelines
We invite designers to submit their concepts based on the following:
• A mockup of the redesigned main wholesale landing page, improving upon our current refinery page (https://halvornkbt.example/refinery/), retaining and enhancing existing words, sections, trust badges, and video placeholders with a luxurious aesthetic.
• A mockup of the industry hub page showcasing all the industries we serve (dental practices, mortuaries, estate attorneys, dentists, pawnshops, jewelry stores, financial advisors).
• At least two examples of industry-specific landing pages (e.g., one for dental practices, improving upon our current dental page (https://halvornkbt.example/refinery/dental-gold/), and one for jewelry stores), showing how the design retains and enhances existing content, incorporates all required sections (trust badges, testimonials, contact info, contact form, shipping info, service bullet points, and video placeholders), and tailors messaging to each audience.
• A brief explanation of your design choices, including how they enhance SEO, tailor messaging for each industry, incorporate and enhance existing content, include the required sections, and align with the luxurious and professional aesthetic we’re seeking.
• Files in HTML, CSS, or Figma format to demonstrate how the design can be implemented.

Judging Criteria
Submissions will be evaluated based on:
• Alignment with the luxurious and professional aesthetic described, significantly improving upon our current designs (https://halvornkbt.example/refinery/ and https://halvornkbt.example/refinery/dental-gold/) while retaining and enhancing existing content.
• Effective retention and enhancement of existing words, sections, trust badges, and video placeholders from our current pages, seamlessly integrating them into the new design.
• Inclusion and effective design of all required sections (trust badges, testimonials, contact info, contact form, shipping info, service bullet points, and video placeholders) on the industry-specific landing pages.
• Creativity and effectiveness in tailoring messaging and visuals for each industry-specific landing page.
• Usability and visual appeal of the industry hub page, including its potential to improve SEO and engage users.
• Suitability for the target audience (high-net-worth wholesale clients in dental, mortuary, legal, pawnshop, jewelry, and financial sectors).
• Compatibility with WordPress and Bricks Builder (based on the format of deliverables).

Additional Notes
• We are open to creative interpretations of “luxury” and encourage designers to think outside the box while maintaining professionalism. Use our current pages as a foundation for content and structure, enhancing and building upon them rather than replacing them entirely.
• The industry hub page should feel intuitive and encourage exploration, potentially using layouts like a grid, carousel, or categorized sections with hover effects.
• Each industry-specific landing page should include a unique value proposition (e.g., “Streamline Your Dental Scrap Refining Process” or “Maximize Value for Your Jewelry Inventory”) to capture attention, building on the clarity of our current dental page but with a more luxurious presentation and all required sections.
• We will provide feedback during the contest and may request revisions from top submissions.

About Us
Halvorn KBT is a leading refinery service provider specializing in precious metals, offering wholesale solutions to a wide range of industries such as dental, jewelry, and legal sectors. Our goal is to create a luxurious online presence that reflects the high value we provide to our clients.
We look forward to seeing your creative designs and how you can bring our vision of a luxurious, industry-focused wholesale section to life!

```html
<!DOCTYPE html>
<html lang="en">
<head>
<meta charset="utf-8">
<title>Refinery Process – Halvorn KBT</title>
<link rel="stylesheet" href="https://fonts.googleapis.com/css2?family=Figtree:wght@400;500;600;700&display=swap">
<style>
:root{
  --ink:#1b1b1b;
  --text:#4a4a4a;
  --muted:#7a7a7a;
  --paper:#ffffff;
  --mist:#f4f4f4;
  --field:#efefef;
  --line:#d9d9d9;
  --night:#1f1f1f;
  --night-2:#232323;
  --gold:#c9a449;
  --gold-soft:#e9cc86;
  --olive:#8a8a4a;
  --blue:#5a7be0;
  --flame:#e0782a;
}
*{box-sizing:border-box;margin:0;padding:0}
html,body{width:1200px;height:4035px;overflow:hidden}
body{position:relative;font-family:"Figtree",Arial,sans-serif;color:var(--ink);background:var(--paper)}
.abs{position:absolute}
a{color:inherit;text-decoration:none}

/* header */
.topbar{left:0;top:0;width:1200px;height:60px;background:#f2f2f2;border-bottom:1px solid var(--line)}
.brand{display:flex;align-items:center;gap:8px;font-size:11px;font-weight:600;letter-spacing:.06em;text-transform:uppercase;color:var(--ink)}
.brand-mark{width:14px;height:14px;border-radius:50%;background:var(--ink)}
.search{left:713px;top:25px;width:188px;height:27px;border:1px solid #bdbdbd;border-radius:8px;background:#fff;font-size:7px;color:#888;padding:8px 12px}
.icon-btn{width:22px;height:22px;display:flex;align-items:center;justify-content:center}
.call-btn{left:978px;top:24px;width:28px;height:28px;border-radius:8px;background:var(--blue)}
.mainnav{left:0;top:60px;width:1200px;height:24px;border-bottom:1px solid var(--line);background:#fff}
.mainnav a{position:absolute;top:5px;font-size:10px;font-weight:500;transform:translateX(-50%)}
.mainnav .dot{position:absolute;top:-2px;right:-5px;width:4px;height:4px;border-radius:50%;background:var(--ink)}

/* hero */
.hero{left:0;top:84px;width:1200px;height:457px;background:#fff;overflow:hidden;border-bottom:1px solid var(--line)}
.hero-swirl{left:72px;top:80px;width:320px;height:130px;background:linear-gradient(90deg,#fafafa,#ececec);border-radius:60px 60px 8px 60px}
.hero-title{left:183px;top:196px;font-size:72px;line-height:70px;font-weight:600;letter-spacing:-.01em}
.hero-photo{left:450px;top:0;width:640px;height:457px;clip-path:polygon(17% 0,98% 0,82% 100%,0 100%);
  background:radial-gradient(ellipse at 40% 40%,#fff1b0 0%,#f5b43a 22%,var(--flame) 42%,#6b2a10 70%,#1c1c1c 100%)}

/* common section parts */
.divider{width:56px;height:22px;display:flex;align-items:center;justify-content:center;gap:6px}
.divider i{display:block;height:1px;width:18px;background:var(--ink)}
.divider b{display:block;width:12px;height:12px;border:1.5px solid var(--ink);transform:rotate(45deg)}
.section-title{font-size:22px;font-weight:500;text-align:center;width:1200px;left:0}
.copy{left:298px;width:606px;text-align:center;font-size:10px;line-height:14px;color:var(--text)}
.copy p{margin-bottom:13px}

.about{left:0;top:541px;width:1200px;height:496px;background:var(--mist)}
.video{left:191px;top:946px;width:816px;height:433px;border-radius:28px;overflow:hidden;
  background:radial-gradient(ellipse at 50% 50%,#d8a93a 0%,#8a6418 32%,#2b2412 62%,#0f0f0f 100%)}
.play{left:345px;top:153px;width:127px;height:127px;border-radius:50%;background:#fff;display:flex;align-items:center;justify-content:center}

.pillars{top:1710px;left:0;width:1200px;height:160px}
.pillar{position:absolute;width:160px;text-align:center;transform:translateX(-50%)}
.gem{width:102px;height:102px;margin:10px auto 0;transform:rotate(45deg);border-radius:3px}
.pillar span{display:block;margin-top:36px;font-size:8px;letter-spacing:.03em;text-transform:uppercase;color:var(--ink)}

/* split */
.split-photo{left:0;top:1933px;width:600px;height:610px;background:radial-gradient(circle at 32% 62%,#ffb347 0%,#c8621c 10%,#8c8c8c 28%,#cfcfcf 60%,#e8e8e8 100%)}
.split-panel{left:600px;top:1933px;width:600px;height:610px;background:var(--night);color:#fff}
.split-panel .divider i{background:#fff}
.split-panel .divider b{border-color:#fff}
.panel-title{left:0;width:600px;top:184px;text-align:center;font-size:21px;font-weight:500}
.panel-rule{left:127px;top:230px;width:348px;height:1px;background:var(--olive)}
.panel-copy{left:140px;width:320px;top:254px;text-align:center;font-size:11.5px;line-height:20px;color:#e4e4e4}
.rail{left:570px;width:2px;background:#6a6a6a}
.coin{width:88px;height:88px;border-radius:50%}

/* registration */
.reg-title{left:0;width:1200px;top:2680px;text-align:center;font-size:46px;font-weight:500}
.step{position:absolute;top:2775px;width:120px;text-align:center;transform:translateX(-50%)}
.step .dot{width:40px;height:40px;border-radius:50%;margin:0 auto;background:#ececec;display:flex;align-items:center;justify-content:center}
.step.is-active .dot{background:var(--ink)}
.step span{display:block;margin-top:16px;font-size:9px;line-height:12px}
.step-link{top:2794px;height:0;border-top:1px dashed #9a9a9a}
.form-title{left:0;width:1200px;top:2909px;text-align:center;font-size:21px;font-weight:500}
.field{position:absolute}
.field label{display:block;font-size:9px;font-weight:500;margin-bottom:6px}
.field label em{color:#d23b3b;font-style:normal}
.field .input{height:39px;background:var(--field);border-radius:2px;position:relative}
.continue{left:906px;top:3198px;width:95px;height:28px;border-radius:14px;background:var(--ink);color:#fff;font-size:10px;font-weight:600;display:flex;align-items:center;justify-content:center;gap:6px}

/* perks */
.perk{top:3317px;width:245px;height:133px;border-radius:18px;padding:36px 24px 0;overflow:hidden}
.perk h3{font-size:14px;font-weight:600}
.perk p{font-size:8px;margin-top:8px;line-height:11px}
.perk a{position:absolute;left:24px;bottom:18px;font-size:8px;font-weight:700;letter-spacing:.04em;text-transform:uppercase}
.perk svg{position:absolute;right:24px;bottom:14px}
.perk-dark{background:var(--night-2);color:#fff}
.perk-dark p{color:#cfcfcf}
.perk-gold{background:linear-gradient(135deg,var(--gold) 0%,var(--gold-soft) 100%);color:var(--ink)}
.perk-gold p{color:#6b5a2a}

/* footer */
.footer{left:0;top:3525px;width:1200px;height:334px;background:var(--night);color:#fff}
.fcol{position:absolute;top:60px}
.fcol h4{font-size:7px;font-weight:400;color:#bdbdbd;margin-bottom:9px}
.fcol li{list-style:none;font-size:8px;line-height:16px}
.hours{left:848px;top:58px;width:152px;height:35px;border:1px solid #888;border-radius:5px;background:#2c2c2c;padding:5px 8px;font-size:9px;font-weight:600;line-height:12px}
.about-note{left:848px;top:106px;width:150px;font-size:9px;line-height:11px;font-weight:500}
.newsletter{left:310px;top:267px;width:260px;text-align:center;font-size:8.5px;line-height:11px;color:#ddd}
.news-input{left:699px;top:286px;width:155px;height:24px;background:#fff;border-radius:2px;font-size:8px;color:#999;padding:6px 7px}
.news-btn{left:863px;top:286px;width:22px;height:24px;background:#2d5bd3;border-radius:3px;display:flex;align-items:center;justify-content:center}
.contact-band{left:0;top:3859px;width:1200px;height:50px;background:#fff;font-size:12px;font-weight:500}
.contact-band span{position:absolute;text-align:center;transform:translateX(-50%)}
.legal{left:0;top:3909px;width:1200px;height:126px;background:var(--night);color:#fff}
.social{display:flex;gap:8px}
.social i{display:block;width:16px;height:16px;border-radius:50%;background:#fff}
</style>
</head>
<body>

<!-- Header -->
<header class="abs topbar">
  <a class="abs brand" href="#" style="left:196px;top:30px">
    <span class="brand-mark"></span>Halvorn KBT Refineries
  </a>
  <div class="abs search">Search for products or categories...</div>
  <span class="abs icon-btn" style="left:911px;top:27px">
    <svg width="16" height="16" viewBox="0 0 16 16" fill="none" stroke="#1b1b1b" stroke-width="1.4"><circle cx="8" cy="8" r="7"/><circle cx="8" cy="6.5" r="2.3"/><path d="M3.5 13c1.2-2 2.7-2.8 4.5-2.8s3.3.8 4.5 2.8"/></svg>
  </span>
  <span class="abs icon-btn" style="left:945px;top:27px">
    <svg width="14" height="16" viewBox="0 0 14 16" fill="#1b1b1b"><path d="M7 0a6 6 0 0 0-6 6c0 4.5 6 10 6 10s6-5.5 6-10a6 6 0 0 0-6-6zm0 8.5A2.5 2.5 0 1 1 7 3.5a2.5 2.5 0 0 1 0 5z"/></svg>
  </span>
  <a class="abs call-btn" href="#" aria-label="Call us" style="display:flex;align-items:center;justify-content:center">
    <svg width="14" height="14" viewBox="0 0 24 24" fill="#fff"><path d="M6.6 10.8a15.1 15.1 0 0 0 6.6 6.6l2.2-2.2a1 1 0 0 1 1-.25 11.4 11.4 0 0 0 3.6.57 1 1 0 0 1 1 1V20a1 1 0 0 1-1 1A17 17 0 0 1 3 4a1 1 0 0 1 1-1h3.5a1 1 0 0 1 1 1c0 1.25.2 2.45.57 3.6a1 1 0 0 1-.25 1z"/></svg>
  </a>
</header>
<nav class="abs mainnav">
  <a href="#" style="left:244px">Gold</a>
  <a href="#" style="left:346px">Silver</a>
  <a href="#" style="left:447px">Shop All</a>
  <a href="#" style="left:548px">Deals<span class="dot"></span></a>
  <a href="#" style="left:650px">Sell to us</a>
  <a href="#" style="left:752px">We Buy</a>
  <a href="#" style="left:854px">IRA</a>
  <a href="#" style="left:956px">Jewelry</a>
</nav>

<!-- Hero -->
<section class="abs hero">
  <div class="abs hero-swirl" role="img" aria-label="Flowing calligraphic flourish above the page title"></div>
  <h1 class="abs hero-title">Refinery<br>Process</h1>
  <div class="abs hero-photo" role="img" aria-label="Molten gold being poured from a glowing crucible"></div>
</section>

<!-- About -->
<section class="abs about">
  <div class="abs divider" style="left:572px;top:83px"><i></i><b></b><i></i></div>
  <h2 class="abs section-title" style="top:125px">About Our Precious Metal Refinery</h2>
  <div class="abs copy" style="top:173px">
    <p>Most refineries are set up to work on precious metals behind closed doors. Here at Halvorn KBT we not only invite you to witness your lot being melted; we encourage you to watch every step of your metals being processed. We have a comfortable waiting area with bulletproof walls and windows for you to witness the melting as it is taking place.</p>
    <p>Our precious metal refinery is equipped with the latest technology and state of the art assaying equipment used to test each lot of your precious metals, ensuring your results are both accurate and precise.</p>
    <p>You will receive an analysis of your metals; certifying the results and giving you peace of mind.</p>
    <p>We take pride in our timeliness and efficiency. We know that time is money and your time is valuable; we will give you your one-day settlement in a matter of hours, with your choice of cash, check or wire transfer. Please call ahead and schedule a same-day appointment at our facility.</p>
  </div>
</section>

<div class="abs video" role="img" aria-label="Video: a gold bar resting on a dark surface flecked with gold">
  <div class="abs play">
    <svg width="18" height="18" viewBox="0 0 18 18"><path d="M5 3l10 6-10 6z" fill="#1b1b1b"/></svg>
  </div>
</div>

<!-- Personal relationships -->
<div class="abs divider" style="left:572px;top:1450px"><i></i><b></b><i></i></div>
<h2 class="abs section-title" style="top:1499px">Personal Relationships</h2>
<div class="abs copy" style="top:1542px">
  <p>We at Halvorn KBT Refineries recognize the value of personal relationships and the details that take service from good to great. We strive to build a personal relationship with our clients. By gaining your confidence and giving consistent accurate results, we work diligently to earn your trust. Ensuring our client's complete satisfaction is our number one goal.</p>
  <p>Halvorn KBT Refineries is built on the idea that trust is the most important asset to a successful business. We strive to earn your trust and confidence every day through transparency, accuracy and personal relationships with each and every client. We recognize that trust is valuable and we at Halvorn KBT want to earn yours.</p>
  <p>Trust can only be earned; give us the opportunity to serve you.</p>
</div>

<section class="abs pillars">
  <a class="pillar" href="#" style="left:329px"><div class="gem" role="img" aria-label="Misty evergreen forest" style="background:linear-gradient(135deg,#d8ddd2,#6d8a6a 60%,#3e5a44)"></div><span>Corporate Responsibility</span></a>
  <a class="pillar" href="#" style="left:511px"><div class="gem" role="img" aria-label="Gold grains in a crucible" style="background:radial-gradient(circle,#f4c542,#9a5a12 55%,#1d1a14)"></div><span>Refining</span></a>
  <a class="pillar" href="#" style="left:691px"><div class="gem" role="img" aria-label="Stacked silver bars" style="background:linear-gradient(135deg,#e5e5e5,#7c7c7c 50%,#222)"></div><span>Minting</span></a>
  <a class="pillar" href="#" style="left:871px"><div class="gem" role="img" aria-label="Market price chart on a dark screen" style="background:linear-gradient(135deg,#3a1f14,#b23a24 55%,#1a0f0c)"></div><span>News &amp; Events</span></a>
</section>

<!-- No middle-man -->
<div class="abs split-photo" role="img" aria-label="Refiner in protective gloves stirring molten metal in a furnace"></div>
<section class="abs split-panel">
  <div class="abs divider" style="left:272px;top:134px"><i></i><b></b><i></i></div>
  <h2 class="abs panel-title">No Middle-Man</h2>
  <div class="abs panel-rule"></div>
  <p class="abs panel-copy">At Halvorn KBT we melt gold and silver received from buying gold and authorized dealers such as pawn shops and we buy gold places. Doesn't it make sense to cut them out? Deal direct with us, we're confident you'll walk out happy!</p>
  <div class="abs rail" style="top:232px;height:42px"></div>
  <div class="abs rail" style="top:283px;height:42px;background:#fff"></div>
  <div class="abs rail" style="top:334px;height:44px"></div>
  <div class="abs coin" role="img" aria-label="Gold buffalo coin" style="left:100px;top:455px;background:radial-gradient(circle at 40% 35%,#f3d77a,#b58a2a 70%,#7a5a18)"></div>
  <div class="abs coin" role="img" aria-label="Silver eagle coin" style="left:204px;top:455px;background:radial-gradient(circle at 40% 35%,#fafafa,#a9a9a9 70%,#6f6f6f)"></div>
  <div class="abs coin" role="img" aria-label="Gold eagle coin" style="left:309px;top:455px;background:radial-gradient(circle at 40% 35%,#f1cf86,#b88a3a 70%,#7a5520)"></div>
  <div class="abs coin" role="img" aria-label="Silver dime-style coin" style="left:414px;top:455px;background:radial-gradient(circle at 40% 35%,#ffffff,#b5b5b5 70%,#777)"></div>
</section>

<!-- Wholesale registration -->
<div class="abs divider" style="left:572px;top:2637px"><i></i><b></b><i></i></div>
<h2 class="abs reg-title">Wholesale Registration</h2>

<div class="abs step-link" style="left:312px;width:109px"></div>
<div class="abs step-link" style="left:469px;width:107px"></div>
<div class="abs step-link" style="left:624px;width:107px"></div>
<div class="abs step-link" style="left:779px;width:107px"></div>

<div class="step is-active" style="left:288px"><div class="dot"><svg width="14" height="16" viewBox="0 0 14 16" fill="none" stroke="#fff" stroke-width="1.3"><rect x="1.5" y="1" width="11" height="14" rx="1"/><path d="M4 5h6M4 8h6M4 11h4"/></svg></div><span>Business Contact<br>Information</span></div>
<div class="step" style="left:445px"><div class="dot"><svg width="14" height="14" viewBox="0 0 14 14" fill="#1b1b1b"><circle cx="7" cy="4" r="3"/><path d="M1 13c.5-3 3-4.5 6-4.5s5.5 1.5 6 4.5z"/></svg></div><span>Primary Owner<br>or Principal</span></div>
<div class="step" style="left:600px"><div class="dot"><svg width="14" height="14" viewBox="0 0 14 14" fill="#1b1b1b"><circle cx="7" cy="4" r="3"/><path d="M1 13c.5-3 3-4.5 6-4.5s5.5 1.5 6 4.5z"/></svg></div><span>Secondary Owner<br>or Principal</span></div>
<div class="step" style="left:755px"><div class="dot"><svg width="12" height="14" viewBox="0 0 12 14" fill="none" stroke="#1b1b1b" stroke-width="1.3"><rect x="1" y="1" width="10" height="12" rx="1"/><path d="M3.5 4.5h5M3.5 7h5M3.5 9.5h5"/></svg></div><span>Billing</span></div>
<div class="step" style="left:910px"><div class="dot"><svg width="16" height="12" viewBox="0 0 16 12" fill="#1b1b1b"><path d="M1 1h9v7H1zM10 4h3l2 2.5V8h-5z"/><circle cx="4" cy="10" r="1.6"/><circle cx="12" cy="10" r="1.6"/></svg></div><span>Shipping</span></div>

<h2 class="abs form-title">Business Contact Information</h2>

<form>
  <div class="field" style="left:197px;top:2962px;width:260px"><label>Legal Business Name<em>*</em></label><div class="input"></div></div>
  <div class="field" style="left:470px;top:2962px;width:260px"><label>Company Phone<em>*</em></label><div class="input"></div></div>
  <div class="field" style="left:743px;top:2962px;width:258px"><label>Email<em>*</em></label><div class="input"></div></div>

  <div class="field" style="left:197px;top:3035px;width:260px"><label>Company Physical Address<em>*</em></label><div class="input"></div></div>
  <div class="field" style="left:470px;top:3035px;width:80px"><label>City<em>*</em></label><div class="input"></div></div>
  <div class="field" style="left:561px;top:3035px;width:78px"><label>State<em>*</em></label><div class="input"></div></div>
  <div class="field" style="left:650px;top:3035px;width:80px"><label>Zip<em>*</em></label><div class="input"></div></div>
  <div class="field" style="left:743px;top:3035px;width:258px"><label>Federal ID/EIN#<em>*</em></label><div class="input"></div></div>

  <div class="field" style="left:197px;top:3110px;width:260px"><label>Date Business Commenced<em>*</em></label><div class="input"></div></div>
  <div class="field" style="left:470px;top:3110px;width:260px"><label>Business Type<em>*</em></label><div class="input"><svg style="position:absolute;right:18px;top:16px" width="8" height="6" viewBox="0 0 8 6" fill="none" stroke="#1b1b1b" stroke-width="1.3"><path d="M1 1l3 3 3-3"/></svg></div></div>
  <div class="field" style="left:743px;top:3110px;width:258px"><label>Website<em>*</em></label><div class="input"></div></div>

  <a class="abs continue" href="#">Continue <svg width="10" height="8" viewBox="0 0 10 8" fill="none" stroke="#fff" stroke-width="1.3"><path d="M1 4h8M6 1l3 3-3 3"/></svg></a>
</form>

<!-- Perks -->
<div class="abs perk perk-dark" style="left:216px">
  <h3>Price match guarantee</h3><p>On all bullion products.</p><a href="#">Learn more</a>
  <svg width="24" height="24" viewBox="0 0 24 24" fill="none" stroke="var(--gold)" stroke-width="1.4"><circle cx="12" cy="12" r="10"/><path d="M7.5 12l3 3 6-6"/></svg>
</div>
<div class="abs perk perk-gold" style="left:478px">
  <h3>100% Insured</h3><p>All orders are tracked, insured, and<br>require a signature.</p>
  <svg width="22" height="24" viewBox="0 0 22 24" fill="none" stroke="#1b1b1b" stroke-width="1.4"><path d="M11 1l9 3.5v7c0 6-4 9.5-9 11.5-5-2-9-5.5-9-11.5v-7z"/><path d="M7 12l3 3 5-5"/></svg>
</div>
<div class="abs perk perk-dark" style="left:738px">
  <h3>Free Shipping</h3><p>Orders ship free over $399.</p><a href="#">Shop now</a>
  <svg width="26" height="20" viewBox="0 0 26 20" fill="none" stroke="var(--gold)" stroke-width="1.4"><path d="M1 2h14v11H1zM15 6h5l4 4v3h-9"/><circle cx="6" cy="16" r="2.2"/><circle cx="19" cy="16" r="2.2"/></svg>
</div>

<!-- Footer -->
<footer class="abs footer">
  <div class="fcol" style="left:199px"><h4>Buying &amp; selling</h4><ul><li>Shop Bullion</li><li>IRA Rollovers</li><li>Silver Bullion</li><li>Gold Bullion</li><li>Platinum Bullion</li><li>Palladium Bullion</li><li>Halvorn Jewelry</li></ul></div>
  <div class="fcol" style="left:362px"><h4>Company</h4><ul><li>Leave a Review</li><li>Testimonials</li><li>Refinery Process</li><li>Blog</li><li>About Us</li></ul></div>
  <div class="fcol" style="left:523px"><h4>Customer care</h4><ul><li>My account</li><li>Investment Tools</li><li>Contact us</li><li>FAQs</li><li>Jewelry 101</li><li>Jewelry Repair</li></ul></div>
  <div class="fcol" style="left:685px"><h4>Legal</h4><ul><li>Privacy Policy</li><li>Terms and Conditions</li><li>Mail-in Terms</li><li>Acceptable Use</li><li>Cookie Policy</li><li>Disclaimer Policy</li><li>Payment Terms</li><li>Shipping Policy</li><li>Returns Policy</li><li>Price Match</li><li>Affiliate Program Terms of Use</li></ul></div>
  <div class="abs hours">Open Mon-Fri<br>10:00a - 6:00p PST</div>
  <p class="abs about-note">Halvorn KBT Refineries is a proudly patriotic Christian business in the United States of America.</p>
  <svg class="abs" style="left:848px;top:160px" width="12" height="20" viewBox="0 0 12 20" fill="#fff"><rect x="5" y="0" width="2.4" height="20"/><rect x="0" y="5" width="12" height="2.4"/></svg>
  <div class="abs" role="img" aria-label="United States flag" style="left:880px;top:162px;width:40px;height:22px;background:linear-gradient(90deg,#2b3e8c 0 40%,#c9323a 40% 100%)"></div>
  <p class="abs newsletter">Subscribe to our newsletter to be the first to know about special deals and promotions.</p>
  <div class="abs news-input">Enter Email</div>
  <div class="abs news-btn"><svg width="12" height="9" viewBox="0 0 12 9" fill="none" stroke="#fff" stroke-width="1.2"><rect x=".6" y=".6" width="10.8" height="7.8"/><path d="M.6.6L6 5l5.4-4.4"/></svg></div>
</footer>

<div class="abs contact-band">
  <span style="left:326px;top:18px">(555) 014-2290</span>
  <span style="left:600px;top:10px;line-height:14px">2140 Larkspur Ave NE,<br>Marlow, OR 97000</span>
  <span style="left:873px;top:18px">info@halvornkbt.example</span>
</div>

<div class="abs legal">
  <div class="abs" style="left:194px;top:16px;display:flex;align-items:center;gap:10px;font-size:9px">
    Follow us on social media to stay up to date:
    <div class="social" aria-label="Social media links"><i></i><i></i><i></i><i></i><i></i></div>
  </div>
  <p class="abs" style="left:194px;top:48px;font-size:9px">© 2025 All Rights Reserved Halvorn KBT Refineries</p>
  <div class="abs brand" style="left:194px;top:80px;color:#fff;font-size:20px;gap:12px">
    <span class="brand-mark" style="width:22px;height:22px;background:#fff"></span>Halvorn KBT Refineries
  </div>
</div>

</body>
</html>
```